TARPLIFT business card design

TARPLIFT is a manufacturer of skip bags supplying both the domestic and commercial market. We wish to convey core characteristics of strength, professionalism and reliability to our customers. We are after a business card that uses our company colours of black and yellow as well as incorporating our logo. Our customers are predominantly in the construction or hardware industry. It is important the cards are professional as we are a small company wishing to appear larger than we actually are. more info on the company and product available at www.tarplift-example.com.au

Target Market(s)

hardware buyers, contruction company owners

Industry/Entity Type

Construction

Requirements
Must have
• company colours of black and yellow - No other colours or variation of yellow black. our company logo. card design must convey "tough"
• Card design must be landscape
• Details to be included on the card are:
• Name and Tiltle
• Phone number : 1300 52 41 63
• Mobile: 0455 817 392
• Fax: 03 9876 4410
• email: dean.harlow@tarplift-example.com.au
• address: PO Box 517, Kelverton, VIC,3999
• Text in white when on a black background
Nice to have
• I like the idea of the back of the card being black with lighter circle area in the middle with black logo in the centre. Similar to the attached "iconic" card

```html
<!DOCTYPE html>
<html lang="en">
<head>
<meta charset="utf-8">
<title>TARPLIFT business card</title>
<link rel="stylesheet" href="https://fonts.googleapis.com/css2?family=Archivo:wght@500;800&display=swap">
<style>
  :root {
    --yellow: #f2cd00;
    --black: #111111;
    --charcoal-light: #5a5a5a;
    --charcoal-dark: #262626;
    --page: #ffffff;
    --text-font: "Archivo", Arial, sans-serif;
  }
  * { margin: 0; padding: 0; box-sizing: border-box; }
  html, body {
    width: 1200px;
    height: 1004px;
    overflow: hidden;
    background: var(--page);
    font-family: var(--text-font);
    color: var(--black);
  }
  .card {
    position: absolute;
    left: 260px;
    width: 680px;
    height: 402px;
    border-radius: 18px;
    overflow: hidden;
  }
  /* Front */
  .card-front {
    top: 70px;
    background: var(--yellow);
  }
  .brand {
    position: absolute;
    left: 44px;
    top: 64px;
    display: flex;
    align-items: center;
    gap: 14px;
  }
  .brand-mark {
    width: 46px;
    height: 46px;
    background: var(--black);
  }
  .brand-name {
    font-weight: 800;
    font-size: 44px;
    letter-spacing: 0.5px;
    line-height: 1;
    color: var(--black);
  }
  .person {
    position: absolute;
    left: 448px;
    top: 38px;
  }
  .person-name {
    font-weight: 800;
    font-size: 23px;
    letter-spacing: 0.3px;
    line-height: 1.1;
  }
  .person-title {
    font-weight: 500;
    font-size: 16px;
    margin-top: 4px;
    letter-spacing: 0.4px;
  }
  .contact {
    position: absolute;
    left: 44px;
    top: 238px;
    font-weight: 500;
    font-size: 17px;
    line-height: 23px;
    list-style: none;
  }
  .contact .address { font-weight: 800; }
  .contact .label {
    display: inline-block;
    width: 34px;
    font-weight: 800;
  }
  /* Back */
  .card-back {
    top: 532px;
    background: radial-gradient(ellipse at center, var(--charcoal-light) 0%, var(--charcoal-dark) 70%);
  }
  .back-disc {
    position: absolute;
    left: 50%;
    top: 50%;
    width: 232px;
    height: 232px;
    margin: -116px 0 0 -116px;
    border-radius: 50%;
    background: var(--yellow);
    display: flex;
    align-items: center;
    justify-content: center;
  }
  .back-disc .brand {
    position: static;
    gap: 9px;
  }
  .back-disc .brand-mark { width: 30px; height: 30px; }
  .back-disc .brand-name { font-size: 30px; }
</style>
</head>
<body>
  <section class="card card-front" aria-label="Card front">
    <div class="brand">
      <span class="brand-mark"></span>
      <span class="brand-name">TARPLIFT</span>
    </div>
    <div class="person">
      <p class="person-name">DEAN HARLOW</p>
      <p class="person-title">MANAGER</p>
    </div>
    <ul class="contact">
      <li class="address">PO Box 517, Kelverton, VIC,3999</li>
      <li><span class="label">T :</span>1300 52 41 63</li>
      <li><span class="label">M:</span>0455 817 392</li>
      <li><span class="label">F:</span>03 9876 4410</li>
      <li><span class="label">E:</span>dean.harlow@tarplift-example.com.au</li>
    </ul>
  </section>

  <section class="card card-back" aria-label="Card back">
    <div class="back-disc">
      <div class="brand">
        <span class="brand-mark"></span>
        <span class="brand-name">TARPLIFT</span>
      </div>
    </div>
  </section>
</body>
</html>
```